Thimble Nook web site

I have been running an online business for 6 years.
www.thimblenook.com.au I specialise in ribbons, buttons and unique craft materials. I sell online to individuals and shops with seperate retail and wholesale sites. The web page I'd like redesigned is my retail site.

It needs a clean, fresh look. I've recently had a new logo designed (thanks pixel harbour!) and want the web site to incorporate the new design and colour scheme of black and white. (new logo attached as a file)

I no longer want the page with the large image www.thimblenook.com.au I want to have the first page as the retail shop homepage.
http://www.thimblenook.com.au/index.php so this page needs to have all the links

I want to the look to be fresh, modern and clear. It needs to be quick to load.

Notes from my IT guru: They need to know that the following tend to remain static with just the content section changing on each page; Header Left column (but different in the cart) right column (if required) footer
Updates

Thanks for your designs. 1/3 of my users use mobile devices so please take that into consideration. I would like the logo to be incorporated into the design and be a prominent feature (most have just used it as a tiny image in the top left corner. I would like it to be larger and more prominent.  thanks                                   

Thanks to all the designers who have submitted. Can you please add  'Boutique craft supplies' near the logo. That is my tag line. Thanks

Target Market(s)

Crafty females of all ages

Industry/Entity Type

Business

Requirements
Must have
• links to;
blog
gallery
chatterloop
snapboardly
wholesale
space for an image which I change approx every 2 weeks
about Thimble Nook
contact
privacy policy
terms and conditions
newsletter sign up
shipping info
product search
Nice to have
• I am not sure if I want product images on the homepage? I have attached a few images.
Should not have
• not too much colour - I hate the green border I have now

```html
<!DOCTYPE html>
<html lang="en">
<head>
<meta charset="utf-8">
<title>Thimble Nook – Boutique craft supplies</title>
<link rel="stylesheet" href="https://fonts.googleapis.com/css2?family=Bitter:wght@400;500&family=Open+Sans:ital,wght@0,300;0,400;0,600;1,400;1,700&family=Arimo:ital,wght@0,400;0,700;1,400&family=Cormorant+Garamond:ital,wght@1,600&display=swap">
<style>
:root{
  --ink:#141414;
  --ink-soft:#333;
  --grey-mid:#777;
  --grey-line:#d4d4d4;
  --hero-light:#e9e9e9;
  --hero-dark:#b3b3b3;
  --paper:#fff;
  --band-top:#e9e9e9;
  --band-bottom:#fbfbfb;
  --bar:#e4e4e4;
  --price:#9b1232;
  --product:#6a1f5c;
  --badge-grey:#a39a96;
  --social-one:#234f79;
  --social-two:#1ea4e6;
  --social-three:#f39a1b;
  --social-four:#ababab;
}
*{box-sizing:border-box;margin:0;padding:0}
html,body{width:1200px;height:1200px;overflow:hidden;background:var(--paper)}
body{position:relative;font-family:"Arimo",Arial,sans-serif;color:var(--ink-soft)}
h2,h3{font-weight:400}
.abs{position:absolute}

/* top bar */
.topbar{left:0;top:0;width:1200px;height:51px;background:var(--ink)}
.nav{font-family:"Bitter",serif;font-size:17px;color:#fff;top:15px;white-space:nowrap}
.nav-sep{top:16px;width:1px;height:20px;background:#3d3d3d}
.search{left:896px;top:11px;width:202px;height:30px;background:#2a2a2a;border:1px solid #555;color:#888;font-family:"Open Sans",sans-serif;font-size:15px;font-weight:300;padding:3px 9px}
.search svg{position:absolute;right:5px;top:4px}

/* hero */
.hero{left:0;top:51px;width:1200px;height:403px;
  background:radial-gradient(ellipse 380px 360px at 240px 60px,#fafafa 0%,var(--hero-light) 35%,transparent 100%),
  linear-gradient(90deg,#c9c9c9 0%,var(--hero-dark) 100%)}
.logo-glow{left:118px;top:22px;width:240px;height:180px;border-radius:50%;background:radial-gradient(ellipse at center,#fff 55%,rgba(255,255,255,0) 72%)}
.brand{left:110px;top:88px;width:256px;text-align:center;font-family:"Bitter",serif;font-weight:400;font-size:38px;line-height:40px;color:var(--ink)}
.tagline{left:110px;top:176px;width:256px;text-align:center;font-family:"Open Sans",sans-serif;font-size:12px;color:var(--grey-mid);letter-spacing:.5px}
.phone{left:855px;top:64px;width:229px;text-align:right;white-space:nowrap;font-family:"Open Sans",sans-serif;font-weight:300;font-size:32px;line-height:40px;color:var(--ink);border-bottom:1px solid #888;padding-bottom:1px}
.phone::before{content:"";position:absolute;left:0;bottom:-1px;width:14px;border-bottom:1px dotted var(--ink)}

.news-title{left:123px;top:240px;font-family:"Open Sans",sans-serif;font-size:31px;line-height:40px;color:var(--ink-soft);white-space:nowrap;letter-spacing:-.2px}
.news-title b{font-weight:600;color:var(--grey-mid)}
.news-rule{left:123px;top:284px;width:260px;height:1px;background:#666}
.news-text{left:123px;top:293px;width:285px;font-family:"Arimo",sans-serif;font-style:italic;font-size:12.5px;line-height:15px;color:var(--ink-soft);letter-spacing:.3px}
.email{left:153px;top:334px;width:247px;height:34px;border:1px solid #f2f2f2;background:linear-gradient(#bdbdbd,#cacaca);font-family:"Open Sans",sans-serif;font-style:italic;font-size:13px;color:#f5f5f5;padding:8px 10px}
.subscribe{left:310px;top:386px;width:89px;height:32px;border-radius:7px;background:linear-gradient(#3a3a3a,#050505);color:#fff;font-family:"Open Sans",sans-serif;font-style:italic;font-weight:700;font-size:14px;text-align:center;line-height:31px}

/* slider */
.slider{left:466px;top:130px;width:615px;height:368px;background:var(--paper)}
.slide{left:473px;top:138px;width:600px;height:352px;
  background:linear-gradient(100deg,#3b3b44 0%,#9aa0a8 12%,#c8203a 24%,#d9475a 32%,#a8cf55 42%,#e7d24a 56%,#f2e089 64%,#cde6ee 74%,#9fd3e3 88%,#5ab5cc 100%)}
.slider-shadow{left:485px;top:496px;width:585px;height:20px;background:radial-gradient(ellipse at top,rgba(0,0,0,.45),rgba(0,0,0,0) 70%)}
.arrow{top:277px;width:74px;height:74px;border-radius:50%;background:rgba(20,20,20,.85)}
.arrow-left{left:429px;clip-path:inset(0 0 0 37px)}
.arrow-right{left:1035px;clip-path:inset(0 28px 0 0)}
.arrow svg{position:absolute;top:25px}

/* about */
.about-title{left:122px;top:488px;font-family:"Bitter",serif;font-size:29px;line-height:36px;color:var(--ink);letter-spacing:.5px;white-space:nowrap}
.about-rule{left:122px;top:531px;width:960px;height:1px;background:var(--grey-line)}
.about-photo{left:123px;top:547px;width:216px;height:144px;border:4px solid #dcdcdc;
  background:linear-gradient(180deg,#eef0ee 0%,#8e9a55 20%,#a2a864 38%,#e6b83a 55%,#eec74e 70%,#d9643b 85%,#3fa1a8 100%)}
.about-text{left:357px;top:545px;width:718px;font-size:12.5px;line-height:20px;color:var(--ink-soft)}
.about-text p+p{margin-top:20px}
.about-text strong{color:var(--ink)}
.more{left:970px;top:696px;width:102px;text-align:right;white-space:nowrap;font-family:"Open Sans",sans-serif;font-size:11px;font-style:italic;font-weight:700;color:var(--ink)}

/* content band */
.band{left:0;top:745px;width:1200px;height:384px;background:linear-gradient(var(--band-top),var(--band-bottom) 45%)}
.band-shadow{left:120px;top:737px;width:960px;height:10px;background:radial-gradient(ellipse at bottom,rgba(0,0,0,.12),rgba(0,0,0,0) 70%)}

.post{width:680px;height:150px}
.badge{left:0;top:0;width:58px;height:86px}
.badge-text{left:0;width:58px;text-align:center;color:#fff;font-family:"Arimo",sans-serif;line-height:1}
.post-title{left:74px;top:6px;font-family:"Bitter",serif;font-size:21px;line-height:28px;color:var(--ink);letter-spacing:.4px;white-space:nowrap}
.post-meta{left:74px;top:39px;font-size:12px;color:#555;letter-spacing:.5px;white-space:nowrap}
.post-meta b{color:var(--ink)}
.post-rule{left:74px;top:57px;width:587px;border-top:1px dotted #999}
.post-body{left:74px;top:68px;width:595px;font-size:12.5px;line-height:19px;color:var(--ink-soft)}
.post-bar{left:74px;top:117px;width:588px;height:28px;background:var(--bar);font-size:12px;font-style:italic;color:var(--ink-soft);padding:7px 8px 0 30px}
.post-bar svg{position:absolute;left:7px;top:8px}
.post-bar .readmore{position:absolute;right:9px;top:7px}

.side-title{left:822px;top:772px;font-family:"Bitter",serif;font-size:21px;line-height:28px;color:var(--ink);letter-spacing:.5px;white-space:nowrap}
.card{left:824px;top:817px;width:219px;height:267px;background:var(--paper);border:1px solid #ddd;border-radius:3px}
.product-photo{left:20px;top:19px;width:173px;height:122px;
  background:linear-gradient(90deg,#9b84c0 0%,#b9df6a 25%,#d7e9a3 45%,#8fc94a 60%,#a48dcb 80%,#7c6aa6 100%)}
.price{left:0;top:140px;width:219px;text-align:center;font-family:"Cormorant Garamond",serif;font-style:italic;font-weight:600;font-size:27px;color:var(--price)}
.product-name{left:0;top:177px;width:219px;text-align:center;font-size:12px;font-weight:700;line-height:18px;color:var(--product)}
.cart{left:63px;top:218px;width:84px;height:28px;border:1px solid #bbb;background:linear-gradient(#fff,#e6e6e6);font-size:12px;font-weight:700;color:#333;text-align:center;line-height:26px}

/* footer */
.footer{left:0;top:1129px;width:1200px;height:71px;background:var(--ink)}
.copyright{left:115px;top:1156px;font-size:12px;color:#9a9a9a;white-space:nowrap;letter-spacing:-.1px}
.legal{left:474px;top:1156px;font-size:12px;color:#fff;white-space:nowrap}
.legal span{color:#aaa;margin:0 9px}
.social{top:1145px;width:38px;height:38px;border-radius:50%;color:#fff;font-family:"Arimo",sans-serif;font-size:6.5px;font-weight:700;text-align:center;line-height:38px;white-space:nowrap;overflow:hidden}
</style>
</head>
<body>

<header>
  <div class="abs topbar"></div>
  <nav>
    <span class="abs nav" style="left:399px">Shop</span>
    <span class="abs nav-sep" style="left:477px"></span>
    <span class="abs nav" style="left:513px">Wholesale</span>
    <span class="abs nav-sep" style="left:628px"></span>
    <span class="abs nav" style="left:661px">Blog</span>
    <span class="abs nav-sep" style="left:729px"></span>
    <span class="abs nav" style="left:766px">Gallery</span>
  </nav>
  <div class="abs search">search
    <svg width="22" height="22" viewBox="0 0 22 22"><circle cx="8.5" cy="8.5" r="6" fill="none" stroke="#fff" stroke-width="2.6"/><line x1="13" y1="13" x2="20" y2="20" stroke="#fff" stroke-width="4" stroke-linecap="round"/></svg>
  </div>
</header>

<section class="hero-area">
  <div class="abs hero"></div>
  <div class="abs logo-glow"></div>
  <div class="abs brand">Thimble<br>Nook</div>
  <div class="abs tagline">Boutique craft supplies</div>
  <div class="abs phone">1300 555 0142</div>

  <div class="abs news-title"><b>Sign up</b> Newsletter</div>
  <div class="abs news-rule"></div>
  <p class="abs news-text">Lorem Ipsum has been the industry's standard dummy text ever since the 1500s</p>
  <div class="abs email">Email Address</div>
  <div class="abs subscribe">Subscribe</div>

  <div class="abs slider"></div>
  <div class="abs slide" role="img" aria-label="Rolls of striped chevron ribbon in black, red, green, yellow, pale blue and turquoise"></div>
  <div class="abs slider-shadow"></div>
  <div class="abs arrow arrow-left"><svg style="left:47px" width="16" height="24" viewBox="0 0 16 24"><polyline points="13,2 3,12 13,22" fill="none" stroke="#fff" stroke-width="3"/></svg></div>
  <div class="abs arrow arrow-right"><svg style="left:15px" width="16" height="24" viewBox="0 0 16 24"><polyline points="3,2 13,12 3,22" fill="none" stroke="#fff" stroke-width="3"/></svg></div>
</section>

<section class="about">
  <h2 class="abs about-title">About Thimble Nook</h2>
  <div class="abs about-rule"></div>
  <div class="abs about-photo" role="img" aria-label="Stack of patterned washi tape rolls in green, yellow and orange"></div>
  <div class="abs about-text">
    <p><strong>Lorem Ipsum has been the industry's standard dummy text ever since the 1500s,</strong> when an unknown printer took a galley of type and scrambled it to make a type specimen book. It has survived not only five centuries, but also the leap into electronic typesetting, remaining essentially unchanged.</p>
    <p>It was popularised in the 1960s with the release of Letraset sheets containing Lorem Ipsum passages, and more recently has survived not only five centuries, but also the leap into electronic typesetting, remaining essentially unchanged. It was popularised in the 1960s with the release of Letraset sheets containing Lorem Ipsum passages.</p>
  </div>
  <div class="abs more">More Details ››</div>
</section>

<div class="abs band"></div>
<div class="abs band-shadow"></div>

<main>
  <article class="abs post" style="left:104px;top:767px">
    <svg class="abs badge" viewBox="0 0 58 86" width="58" height="86">
      <circle cx="29" cy="57" r="26" fill="#1a1a1a" stroke="#1a1a1a" stroke-width="3" stroke-dasharray="3 3"/>
      <circle cx="29" cy="27" r="26" fill="var(--badge-grey)" stroke="var(--badge-grey)" stroke-width="3" stroke-dasharray="3 3"/>
    </svg>
    <div class="abs badge-text" style="top:13px;font-size:12px">Dec</div>
    <div class="abs badge-text" style="top:27px;font-size:17px;font-weight:700">13th</div>
    <div class="abs badge-text" style="top:57px;font-size:12px;font-weight:700">2011</div>
    <h3 class="abs post-title">Starling yaml config file</h3>
    <div class="abs post-meta">April 21st, 2009 — <b>Uncategorized</b></div>
    <div class="abs post-rule"></div>
    <p class="abs post-body">I had a bit of trouble figuring how this should look like. Ended up finding it here. Basically, it should look something like:I had a bit of trouble figuring how this should look like. Ended up finding it here.</p>
    <div class="abs post-bar"><svg width="18" height="12" viewBox="0 0 18 12"><ellipse cx="9" cy="5" rx="9" ry="5" fill="#999"/><polygon points="4,8 3,12 8,9" fill="#999"/></svg>$ Comments<span class="readmore">Readmore [+]</span></div>
  </article>

  <article class="abs post" style="left:100px;top:933px">
    <svg class="abs badge" viewBox="0 0 58 86" width="58" height="86">
      <circle cx="29" cy="57" r="26" fill="#1a1a1a" stroke="#1a1a1a" stroke-width="3" stroke-dasharray="3 3"/>
      <circle cx="29" cy="27" r="26" fill="var(--badge-grey)" stroke="var(--badge-grey)" stroke-width="3" stroke-dasharray="3 3"/>
    </svg>
    <div class="abs badge-text" style="top:13px;font-size:12px">Dec</div>
    <div class="abs badge-text" style="top:27px;font-size:17px;font-weight:700">13th</div>
    <div class="abs badge-text" style="top:57px;font-size:12px;font-weight:700">2011</div>
    <h3 class="abs post-title">Starling yaml config file</h3>
    <div class="abs post-meta">April 21st, 2009 — <b>Uncategorized</b></div>
    <div class="abs post-rule"></div>
    <p class="abs post-body">I had a bit of trouble figuring how this should look like. Ended up finding it here. Basically, it should look something like:I had a bit of trouble figuring how this should look like. Ended up finding it here.</p>
    <div class="abs post-bar"><svg width="18" height="12" viewBox="0 0 18 12"><ellipse cx="9" cy="5" rx="9" ry="5" fill="#999"/><polygon points="4,8 3,12 8,9" fill="#999"/></svg>$ Comments<span class="readmore">Readmore [+]</span></div>
  </article>
</main>

<aside>
  <h3 class="abs side-title">Wholesale Products</h3>
  <div class="abs card">
    <div class="abs product-photo" role="img" aria-label="Bundle of lime green and lilac lace ribbons"></div>
    <div class="abs price">$360.00</div>
    <div class="abs product-name">LUMIERE Velour<br>(EDP, 100ml)</div>
    <div class="abs cart">Add to cart</div>
  </div>
</aside>

<footer>
  <div class="abs footer"></div>
  <div class="abs copyright">© Copyright 2013 NORTHGATE STUDIO - All Rights Reserved</div>
  <div class="abs legal">Privacy Policy<span>|</span>Terms &amp; Conditions</div>
  <div class="abs social" style="left:908px;background:var(--social-one)">chatterloop</div>
  <div class="abs social" style="left:955px;background:var(--social-two)">tweetlark</div>
  <div class="abs social" style="left:1002px;background:var(--social-three)">
    <svg style="margin-top:11px" width="16" height="16" viewBox="0 0 16 16"><circle cx="3" cy="13" r="2" fill="#fff"/><path d="M1 7a8 8 0 0 1 8 8" fill="none" stroke="#fff" stroke-width="2.2"/><path d="M1 2a13 13 0 0 1 13 13" fill="none" stroke="#fff" stroke-width="2.2"/></svg>
  </div>
  <div class="abs social" style="left:1048px;background:var(--social-four)">
    <svg style="margin-top:13px" width="18" height="12" viewBox="0 0 18 12"><rect x="0" y="0" width="18" height="12" fill="#fff"/><polyline points="0,0 9,7 18,0" fill="none" stroke="#ababab" stroke-width="1.5"/></svg>
  </div>
</footer>

</body>
</html>
```